Tolvex Engineers: Why you should hire us keepsake

New design. Open to plastic cards. We are an engineering firm that designs cell phone towers and commercial buildings. Please check out our website www.tolvexgrp.com for more details. We want people to remember our card and for it to be useful if possible. We want the same look and feel on these cards to be translated to other marketing material we may need such as brochures.

Target Market(s)

Architects, Developers and Telecommunication Carriers

Industry/Entity Type

Engineering

Contact Information for Business Card

Card with our company colors, logo, and innovative design with elements related to our industry.

Font styles to use
Sans Serif

Colors
9bcb3c
abd036
0255a3

Requirements
Must have
• Sleek and hip design
Nice to have
• Bright lime green and navy coloring that pops with an innovative design.
Should not have
• A basic and boring design

```html
<!DOCTYPE html>
<html lang="en">
<head>
<meta charset="utf-8">
<title>Tolvex Engineers Business Card</title>
<link rel="stylesheet" href="https://fonts.googleapis.com/css2?family=Open+Sans:wght@400;700;800&display=swap">
<style>
  :root {
    --backdrop: #3a3431;
    --card: #0b0b0b;
    --lime: #2fe52a;
    --ink-light: #d9d9d9;
    --divider: #3c3c3c;
  }
  * { margin: 0; padding: 0; box-sizing: border-box; }
  html, body { width: 1200px; height: 844px; overflow: hidden; }
  body {
    background: var(--backdrop);
    font-family: "Open Sans", Arial, sans-serif;
    position: relative;
  }
  .card {
    position: absolute;
    top: 272px;
    width: 525px;
    height: 300px;
    background: var(--card);
    border-radius: 3px;
    box-shadow: 0 8px 24px rgba(0,0,0,.45);
  }
  .card--contact { left: 50px; }
  .card--brand { left: 625px; }

  .wordmark {
    position: absolute;
    color: var(--lime);
    font-weight: 800;
    line-height: 1;
    letter-spacing: -0.5px;
  }
  .card--contact .wordmark {
    left: 36px;
    top: 146px;
    width: 190px;
    font-size: 30px;
    line-height: 1.05;
  }
  .wordmark-line { display: block; white-space: nowrap; }
  .divider {
    position: absolute;
    left: 240px;
    top: 70px;
    width: 1px;
    height: 160px;
    background: var(--divider);
  }
  .person-name {
    position: absolute;
    left: 268px;
    top: 72px;
    color: var(--lime);
    font-size: 17px;
    font-weight: 400;
    letter-spacing: .3px;
    text-transform: uppercase;
    white-space: nowrap;
  }
  .contact-list {
    position: absolute;
    left: 268px;
    top: 122px;
    list-style: none;
  }
  .contact-list li {
    display: flex;
    align-items: center;
    gap: 9px;
    color: var(--ink-light);
    font-size: 13px;
    line-height: 21px;
    white-space: nowrap;
  }
  .contact-list svg { width: 11px; height: 11px; fill: var(--lime); flex: none; }

  .card--brand .wordmark {
    left: 0; right: 0;
    top: 104px;
    text-align: center;
    font-size: 40px;
    white-space: nowrap;
  }
  .tagline {
    position: absolute;
    left: 0; right: 0;
    top: 196px;
    text-align: center;
    color: var(--lime);
    font-size: 11px;
    letter-spacing: .4px;
    text-transform: uppercase;
  }
</style>
</head>
<body>
  <section class="card card--contact">
    <div class="wordmark">
      <span class="wordmark-line">Tolvex</span>
      <span class="wordmark-line">Engineers</span>
    </div>
    <div class="divider"></div>
    <h1 class="person-name">Dana Hollis Marren</h1>
    <ul class="contact-list">
      <li>
        <svg viewBox="0 0 12 12" aria-hidden="true"><path d="M1 3.5C1 2 2.5 1 6 1s5 1 5 2.5V5H8.5V4h-5v1H1zM2.5 6h7l1 5h-9z"/></svg>
        555.014.2230
      </li>
      <li>
        <svg viewBox="0 0 12 12" aria-hidden="true"><path d="M3 0h6v12H3zM4 1.5v8h4v-8z"/></svg>
        555.017.4418
      </li>
      <li>
        <svg viewBox="0 0 12 12" aria-hidden="true"><path d="M0 2h12v8H0zM1 3l5 3.5L11 3v-.2H1z" fill-rule="evenodd"/></svg>
        DMARREN@tolvexgrp.com
      </li>
      <li>
        <svg viewBox="0 0 12 12" aria-hidden="true"><circle cx="6" cy="6" r="5"/></svg>
        www.tolvexgrp.com
      </li>
    </ul>
  </section>

  <section class="card card--brand">
    <div class="wordmark">Tolvex Engineers</div>
    <p class="tagline">Multi-Displine Engineering</p>
  </section>
</body>
</html>
```